MoveNest Landing Page

We need to freshen up our homepage.

The company is MoveNest.com. We provide cloud-based management software for class venues - dance, yoga, martial arts, etc.

The challenge here is to create something that's simultaneously lighthearted and professional. We want our customers to know that the software is easy, fun and non-intimidating, but also powerful enough to handle whatever they throw at it.

Page content can remain the same as it is now. Feel free to move things around, manipulate it however you like.

We like our logo, but feel free to manipulate it as part of your design. Fonts used in the logo are Futura Extra Bold and Rockwell.

NOTE: The default screenshot in the homepage video is NOT our branding choice, it just happens to be the default freeze frame from vidloop.. Feel free to ignore it altogether in your design. We are not affiliated with that character, or the app that we used to create the vid.
Updates

Project Deadline Extended
Reason: We are extending this contest by request. Out of 65 designs, so far we only really like 4. There's still a good chance to win this contract! Please submit your very best :) Owen

Target Market(s)

Studio owners who are not necessarily tech savvy.

Industry/Entity Type

Software

Requirements
Must have
• Look and feel of a modern web app.

Delivery in a layered PSD.

```html
<!DOCTYPE html>
<html lang="en">
<head>
<meta charset="utf-8">
<title>MoveNest – Manage your classes online</title>
<link rel="stylesheet" href="https://fonts.googleapis.com/css2?family=Open+Sans:wght@300;400;600;700;800&family=Caveat:wght@400;600&display=swap">
<style>
  :root {
    --page-bg: #f1f1f1;
    --header-bg: #ffffff;
    --header-line: #e2e2e2;
    --brand-blue: #3b6194;
    --nav-grey: #8a8a8a;
    --nav-green: #7bb72f;
    --nav-orange: #e9a23b;
    --board-green: #3f7b6d;
    --board-green-dark: #2f6558;
    --headline: #eef4f1;
    --chalk-green: #a9d46a;
    --button-orange: #e8a23c;
    --band-pale: #cbd8e7;
    --band-blue: #8199bd;
    --band-grey: #d7d8da;
    --band-text: #4a4a4a;
    --card-bg: #ffffff;
    --standard-green: #8dc63f;
    --premium-brown: #8c7b5a;
    --premium-grey: #585858;
    --bullet-text: #6a6a6a;
    --photo-light: #f4f1ee;
    --photo-mid: #cdbfb3;
  }
  * { margin: 0; padding: 0; box-sizing: border-box; }
  html, body { width: 1200px; height: 893px; overflow: hidden; }
  body {
    position: relative;
    background: var(--page-bg);
    font-family: "Open Sans", Arial, sans-serif;
  }

  /* Header */
  .site-header {
    position: absolute; left: 0; top: 0; width: 1200px; height: 44px;
    background: var(--header-bg);
    border-bottom: 1px solid var(--header-line);
  }
  .brand {
    position: absolute; left: 183px; top: 7px;
    font-weight: 800; font-size: 25px; letter-spacing: 0.5px;
    color: var(--brand-blue); line-height: 30px;
  }
  .main-nav {
    position: absolute; right: 222px; top: 15px;
    display: flex; gap: 26px;
    font-size: 10.5px; font-weight: 700; letter-spacing: 0.3px;
  }
  .main-nav a { text-decoration: none; color: var(--nav-grey); }
  .main-nav .nav-login { color: var(--nav-green); }
  .main-nav .nav-signup { color: var(--nav-orange); }

  /* Hero */
  .hero {
    position: absolute; left: 0; top: 44px; width: 1200px; height: 327px;
    background: radial-gradient(ellipse at 45% 40%, var(--board-green) 0%, var(--board-green-dark) 100%);
    overflow: hidden;
  }
  .hero-headline {
    position: absolute; left: 164px; top: 52px;
    font-weight: 300; font-size: 24px; line-height: 29px;
    color: var(--headline);
  }
  .signup-button {
    position: absolute; left: 312px; top: 160px;
    width: 102px; height: 38px; border-radius: 19px;
    background: var(--button-orange);
    color: #fff; font-size: 20px; font-weight: 400;
    display: flex; align-items: center; justify-content: center;
    text-decoration: none;
  }
  .signup-accent { position: absolute; left: 408px; top: 150px; }
  .hero-note {
    position: absolute; left: 290px; top: 260px;
    font-family: "Caveat", cursive;
    font-size: 22px; line-height: 25px;
    color: var(--chalk-green); transform: rotate(-6deg);
    text-align: center;
  }
  .hero-photo {
    position: absolute; left: 712px; top: 0; width: 300px; height: 327px;
    background: linear-gradient(180deg, var(--photo-mid) 0%, var(--photo-light) 55%, var(--photo-light) 100%);
    opacity: 0.9;
  }

  /* Intro band */
  .intro-band {
    position: absolute; left: 0; top: 371px; width: 1200px; height: 94px;
    background: var(--band-grey);
  }
  .intro-band::before {
    content: ""; position: absolute; left: 0; top: 0; width: 140px; height: 94px;
    background: var(--band-pale);
  }
  .intro-label {
    position: absolute; left: 140px; top: 0; width: 280px; height: 94px;
    color: #fff;
  }
  .intro-label svg { position: absolute; left: 0; top: 0; }
  .intro-label h2 {
    position: absolute; left: 60px; top: 14px;
    font-size: 27px; line-height: 30px; font-weight: 300;
  }
  .intro-label h2 strong { display: block; font-weight: 700; }
  .intro-text {
    position: absolute; left: 440px; top: 20px; width: 560px;
    font-size: 12px; line-height: 17px; color: var(--band-text);
  }

  /* Plans */
  .plans {
    position: absolute; left: 140px; top: 495px;
    display: flex; gap: 8px;
  }
  .plan {
    height: 150px;
    background: var(--card-bg);
    border-radius: 6px;
    padding: 12px 20px;
    box-shadow: 0 1px 3px rgba(0,0,0,0.06);
  }
  .plan-standard { width: 276px; }
  .plan-premium { width: 284px; }
  .plan-premium-plus { width: 287px; margin-left: 8px; }
  .plan h3 {
    font-weight: 300; font-size: 34px; line-height: 38px; letter-spacing: 0.5px;
  }
  .plan-standard h3 { color: var(--standard-green); }
  .plan-premium h3 { color: var(--premium-brown); }
  .plan-premium-plus h3 { color: var(--premium-grey); }
  .plan-sub {
    font-size: 11px; color: var(--standard-green); line-height: 13px;
  }
  .plan-features { list-style: none; margin-top: 24px; }
  .plan-features li {
    position: relative; padding-left: 10px;
    font-size: 11.5px; line-height: 19px; color: var(--bullet-text);
  }
  .plan-features li::before {
    content: ""; position: absolute; left: 0; top: 8px;
    width: 4px; height: 4px; border-radius: 50%;
    background: var(--standard-green);
  }
  .plan-premium .plan-features li::before { background: var(--premium-brown); }
  .plan-premium-plus .plan-features li::before { background: var(--premium-grey); }
</style>
</head>
<body>
  <header class="site-header">
    <div class="brand">MoveNest</div>
    <nav class="main-nav">
      <a href="#">HOME</a>
      <a href="#">HELP</a>
      <a href="#" class="nav-login">LOGIN</a>
      <a href="#" class="nav-signup">SIGN UP</a>
    </nav>
  </header>

  <section class="hero">
    <h1 class="hero-headline">The easiest way to manage your classes<br>and accept payments online.</h1>
    <a href="#" class="signup-button">Sign Up</a>
    <svg class="signup-accent" width="30" height="50" viewBox="0 0 30 50" aria-hidden="true">
      <line x1="4" y1="28" x2="18" y2="12" stroke="var(--button-orange)" stroke-width="3"/>
      <line x1="4" y1="28" x2="16" y2="42" stroke="var(--button-orange)" stroke-width="3"/>
      <circle cx="19" cy="10" r="5" fill="var(--button-orange)"/>
      <circle cx="17" cy="44" r="5" fill="var(--button-orange)"/>
    </svg>
    <p class="hero-note">5 Minute Setup!<br>It's Free :)</p>
    <div class="hero-photo" role="img" aria-label="Photo of a smiling teacher with folded arms in front of a chalkboard"></div>
  </section>

  <section class="intro-band">
    <div class="intro-label">
      <svg width="280" height="94" viewBox="0 0 280 94" aria-hidden="true">
        <polygon points="0,0 262,0 280,47 262,94 0,94" fill="var(--band-blue)"/>
      </svg>
      <h2>What is <strong>MoveNest?</strong></h2>
    </div>
    <p class="intro-text">MoveNest is the easiest and most affordable way to manage your class studio or venue. We help simplify your daily tasks by leveraging the power of the internet, saving you time and money. Anyone can learn to use MoveNest with our clean, common-sense website.</p>
  </section>

  <section class="plans">
    <article class="plan plan-standard">
      <h3>STANDARD</h3>
      <ul class="plan-features">
        <li>Fully functional scheduling tool</li>
        <li>Filters for easy viewing</li>
      </ul>
    </article>
    <article class="plan plan-premium">
      <h3>PREMIUM</h3>
      <p class="plan-sub">Entire Standard Package, plus....</p>
      <ul class="plan-features">
        <li>3 User Accounts</li>
        <li>Simultaneous Logins</li>
      </ul>
    </article>
    <article class="plan plan-premium-plus">
      <h3>PREMIUM</h3>
      <p class="plan-sub">Entire Premium Package, plus....</p>
      <ul class="plan-features">
        <li>Powerful Point of Sale System</li>
        <li>Accept Credit Cards Immediately</li>
      </ul>
    </article>
  </section>
</body>
</html>
```